Create a newspaper layout from word files and photos provided for wedding

For our wedding we want a "newspaper style" memento for guests. It will include articles I have written about me and my fiancee and our family and friends as well as photos and anecdotes.
We require someone to take our words and design content and turn it into a file that we can get printed.
We will provde content - we want your layout skill.

Full file is available at
https://www.filecrate.example/sh/q7wkbr2m41xpt9/ZZQmTLrhWvkpFGsYcNbVdEoUx?oref=e&n=715204368

Instructions are included.Utilise written content to create wedding newspaper and add photos were possible.
Black and white but photos should be in colour.
Must be 4 or 8 pages.
If text provided is too long notes to be provided to us where cuts are required.

We have committed payment.
We seek designs to review on Sunday evening.
We will select designs at this time or earlier if appropriate design is submitted using full layout.
Once selected we will work with designer to refine and finalise job by Tuesday next week when it must go to printer.

Thanks and if there are an questions post away.

Reason: Extended deadline due to file changes. We require the file to be available to select from by Sunday 12 April 8pm - ignore the Thursday deadline.

Target Market(s)

Wedding guests

Industry/Entity Type

Wedding

Font styles to use
Serif

Requirements
Must have
• Style and photographs
Should not have
• Too much blank space
• Too small text

```html
<!DOCTYPE html>
<html lang="en">
<head>
<meta charset="utf-8">
<title>The Wedding Press</title>
<link rel="stylesheet" href="https://fonts.googleapis.com/css2?family=UnifrakturMaguntia&family=Tinos:wght@400;700&family=Roboto:wght@700;900&display=swap">
<style>
  :root {
    --paper: #fdfbfb;
    --ink: #111111;
    --rule: #1a1a1a;
    --ornament: #d9d6d6;
    --photo-a: #9fc3d6;
    --photo-b: #6b5a66;
    --photo-c: #c9a58f;
  }
  * { margin: 0; padding: 0; box-sizing: border-box; }
  html, body { width: 848px; height: 1200px; overflow: hidden; background: var(--paper); }
  .page { position: relative; width: 848px; height: 1200px; background: var(--paper); color: var(--ink); font-family: "Tinos", "Times New Roman", serif; }

  .edition, .dateline { position: absolute; top: 22px; font-size: 18px; letter-spacing: 0.2px; }
  .edition { left: 40px; }
  .dateline { right: 46px; }

  .masthead-rules { position: absolute; left: 0; top: 0; }
  .ornament { position: absolute; background: var(--ornament); border-radius: 4px; }
  .masthead-title {
    position: absolute; left: 60px; width: 728px; top: 68px;
    text-align: center; font-family: "UnifrakturMaguntia", serif; font-weight: 400;
    font-size: 86px; line-height: 1; letter-spacing: 1px;
  }

  .photo {
    position: absolute; display: flex; align-items: center; justify-content: center;
    font-family: "Tinos", "Times New Roman", serif; color: #1b1b1b;
  }
  .photo--lead { left: 40px; top: 215px; width: 456px; height: 282px;
    background: linear-gradient(120deg, var(--photo-c) 0%, var(--photo-a) 45%, var(--photo-b) 100%);
    font-size: 42px; padding-top: 40px; }
  .photo--strip { left: 311px; top: 975px; width: 488px; height: 122px;
    background: linear-gradient(90deg, var(--photo-a), var(--photo-c) 30%, var(--photo-b) 55%, var(--photo-a) 80%, var(--photo-c));
    font-size: 42px; }

  .headline { position: absolute; left: 505px; width: 300px; top: 212px; text-align: center;
    font-family: "Roboto", Arial, sans-serif; font-weight: 700; line-height: 1; }
  .headline__names { font-size: 70px; line-height: 1.5; }
  .headline__verb { font-size: 42px; margin-top: 6px; }
  .headline__when { font-size: 34px; margin-top: 12px; }

  .party-title { position: absolute; left: 40px; width: 255px; top: 592px; text-align: center;
    font-family: "UnifrakturMaguntia", serif; font-weight: 400; font-size: 27px; }
  .rundown { position: absolute; left: 40px; width: 242px; top: 634px; text-align: center; }
  .rundown__event { margin-bottom: 26px; }
  .rundown__heading { font-weight: 700; font-size: 18px; line-height: 22px; }
  .rundown__item { font-size: 15.5px; line-height: 23px; }
  .rundown__item--tight { line-height: 20px; }

  .story { position: absolute; left: 318px; top: 523px; width: 483px; height: 432.6px; overflow: hidden;
    font-size: 14.6px; line-height: 20.6px; text-align: justify; }
  .story__dropcap { font-family: "UnifrakturMaguntia", serif; font-size: 30px; line-height: 0; }
</style>
</head>
<body>
<div class="page">
  <div class="edition">SPECIAL EDITION</div>
  <div class="dateline">Month dd, yyyy</div>

  <svg class="masthead-rules" width="848" height="200" viewBox="0 0 848 200" aria-hidden="true">
    <g stroke="var(--rule)" stroke-width="2" fill="var(--rule)">
      <line x1="98" y1="55" x2="360" y2="55"/><line x1="488" y1="55" x2="752" y2="55"/>
      <line x1="98" y1="178" x2="360" y2="178"/><line x1="488" y1="178" x2="752" y2="178"/>
      <polygon points="86,55 100,51 100,59"/><polygon points="764,55 750,51 750,59"/>
      <polygon points="86,178 100,174 100,182"/><polygon points="764,178 750,174 750,182"/>
    </g>
  </svg>
  <div class="ornament" style="left:366px;top:34px;width:116px;height:26px" role="img" aria-label="Scroll ornament"></div>
  <div class="ornament" style="left:366px;top:172px;width:116px;height:28px" role="img" aria-label="Scroll ornament"></div>
  <div class="ornament" style="left:40px;top:50px;width:40px;height:136px" role="img" aria-label="Corner flourish"></div>
  <div class="ornament" style="left:768px;top:50px;width:40px;height:136px" role="img" aria-label="Corner flourish"></div>
  <h1 class="masthead-title">The Wedding Press</h1>

  <div class="photo photo--lead" role="img" aria-label="Photo of the couple">Your Photo Here</div>

  <div class="headline">
    <div class="headline__names">NAME &amp;<br>NAME</div>
    <div class="headline__verb">ARE GETTING</div>
    <div class="headline__when">MARRIED TODAY!</div>
  </div>

  <div class="ornament" style="left:36px;top:524px;width:260px;height:150px;background:transparent;border:14px solid var(--ornament);border-bottom:none;border-radius:60px 60px 0 0" role="img" aria-label="Floral frame ornament"></div>
  <h2 class="party-title">Wedding Party</h2>

  <div class="rundown">
    <div class="rundown__event"><div class="rundown__heading">Wedding Events</div><div class="rundown__item">Put your rundown here</div><div class="rundown__item">Put your rundown here</div></div>
    <div class="rundown__event"><div class="rundown__heading">Wedding Events</div><div class="rundown__item">Put your rundown here</div><div class="rundown__item">Put your rundown here</div></div>
    <div class="rundown__event"><div class="rundown__heading">Wedding Events</div><div class="rundown__item">Put your rundown here</div><div class="rundown__item">Put your rundown here</div></div>
    <div class="rundown__event"><div class="rundown__heading">Wedding Events</div><div class="rundown__item">Put your rundown here</div></div>
    <div class="rundown__event"><div class="rundown__heading">Wedding Events</div><div class="rundown__item rundown__item--tight">Put your rundown here</div><div class="rundown__item rundown__item--tight">Put your rundown here</div></div>
    <div class="rundown__event"><div class="rundown__heading">Wedding Events</div><div class="rundown__item">Put your rundown here</div></div>
  </div>
  <div class="ornament" style="left:32px;top:1030px;width:264px;height:150px;background:transparent;border:14px solid var(--ornament);border-top:none;border-radius:0 0 60px 60px" role="img" aria-label="Floral frame ornament"></div>

  <p class="story"><span class="story__dropcap">Y</span>our story here your story here your story here your story here your story here your story here your story here your story here your story here your story here your story here your story here your story here your story here your story here your story here your story here your story here your story here your story here your story here your story here your story here your story here your story here your story here your story here your story here your story here your story here your story here your story here your story here your story here your story here your story here your story here your story here your story here your story here your story here your story here your story here your story here your story here your story here your story here your story here your story here your story here your story here your story here your story here your story here your story here your story here your story here your story here your story here your story here your story here your story here your story here your story here your story here your story here your story here your story here your story here your story here your story here your story here your story here your story here your story here your story here your story here your story here your story here your story here your story here your story here your story here your story here your story here your story here your story here your story here your story here your story here your story here your story here your story here your story here your story here your story here your story here your story here your story here your story here your story here your story here your story here your story here your story here your story here your story here your story here your story here your story here your story here your story here your story here your story here your story here your story here your story here your story here your story here your story here your story here your story here your story here your story here your story here your story here your story here your story here your story here your story here your story here your story here your story here your story here your story here your story here your story here your story here your story here your story here your story here your story here your story here your story here your story here your story here your story here your story here your story here your story here your story here your story here your story here your story here your story here your story here your story here your story here your story here your story here your story here your story here your story here your story here your story here your story here your story here.</p>

  <div class="photo photo--strip" role="img" aria-label="Strip of couple photos">Your Photo Here</div>
</div>
</body>
</html>
```